New Business card design to reflect rebrand

I would like a business card design with a good base colour for our new logo and also a placeholder for a profile pic of the card holder. the design needs to be editable to the point that we can easily change the picture of the person and use that design for printlarkly etc. we are looking at a metalic finish business card so will need a good base colour to bring out the finish.

Target Market(s)

prospective customers

Industry/Entity Type

Business

Contact Information for Business Card

I would like one editable design that we can change the name of the card holder and profile picture. The design need to be in a format that be send to printlarkly etc.

Our address is Fenwick Lodge, Mill Lane, Ashcombe Vale, KT14 3WB Tel no. 01632 960418

Requirements
Must have
• place holder for a profile pic for the card holder. in AI or preferably PSD format

```html
<!DOCTYPE html>
<html lang="en">
<head>
<meta charset="utf-8">
<title>Corvane Workplace Services – Business Card</title>
<link rel="stylesheet" href="https://fonts.googleapis.com/css2?family=Montserrat:wght@600&family=Roboto+Condensed:wght@400&display=swap">
<style>
  :root {
    --page-bg-top: #a9aeb4;
    --page-bg-bottom: #25282c;
    --navy: #1d3a7a;
    --back-start: #0b1670;
    --back-end: #2a0c10;
    --brand-red: #f21d00;
    --red-deep: #ee1a00;
    --white: #ffffff;
    --frame-black: #111111;
    --photo-grey: #e6e6e6;
    --photo-label: #b01800;
    --back-name: #4a5fd0;
  }
  * { box-sizing: border-box; margin: 0; padding: 0; }
  html, body { width: 1200px; height: 1200px; overflow: hidden; }
  body {
    background: linear-gradient(170deg, var(--page-bg-top), var(--page-bg-bottom));
    display: flex;
    flex-direction: column;
    align-items: center;
    justify-content: center;
    gap: 40px;
  }
  .card {
    width: 960px;
    height: 549px;
    position: relative;
    overflow: hidden;
    box-shadow: 0 10px 30px rgba(0,0,0,.35);
  }

  /* Back of card */
  .card-back {
    background: linear-gradient(135deg, var(--back-start), #1a1250 45%, var(--back-end));
    display: flex;
    align-items: center;
    justify-content: center;
  }
  .brand-name {
    font-family: "Montserrat", sans-serif;
    font-weight: 600;
    text-align: center;
    line-height: 1;
  }
  .brand-name .primary { display: block; font-size: 88px; letter-spacing: 2px; }
  .brand-name .secondary { display: block; font-size: 27px; letter-spacing: 9px; margin-top: 14px; }
  .card-back .brand-name { color: var(--back-name); }

  /* Front of card */
  .card-front { display: flex; background: var(--white); }
  .front-brand {
    width: 50%;
    display: flex;
    align-items: center;
    justify-content: center;
  }
  .card-front .brand-name { color: var(--navy); }
  .card-front .brand-name .primary { font-size: 66px; }
  .card-front .brand-name .secondary { font-size: 21px; letter-spacing: 6px; margin-top: 12px; }

  .front-details {
    width: 50%;
    background: linear-gradient(160deg, var(--brand-red), var(--red-deep));
    padding: 50px 40px 0 30px;
    color: var(--white);
    font-family: "Roboto Condensed", sans-serif;
  }
  .photo-placeholder {
    width: 200px;
    height: 260px;
    background: var(--white);
    padding: 5px;
  }
  .photo-frame {
    width: 100%;
    height: 100%;
    border: 6px solid var(--frame-black);
    background: linear-gradient(150deg, #f2f2f2, var(--photo-grey));
    display: flex;
    align-items: center;
    justify-content: center;
  }
  .photo-label {
    transform: rotate(-45deg);
    font-family: "Montserrat", sans-serif;
    font-weight: 600;
    font-size: 36px;
    letter-spacing: 6px;
    color: var(--photo-label);
  }
  .holder-name { font-size: 24px; margin-top: 22px; letter-spacing: .3px; }
  .divider { height: 1px; background: rgba(255,255,255,.45); margin: 24px 0 16px; }
  .phone { font-size: 27px; }
  .address { font-size: 25px; line-height: 1.35; margin-top: 28px; }
</style>
</head>
<body>

  <section class="card card-back" aria-label="Business card back">
    <div class="brand-name">
      <span class="primary">CORVANE</span>
      <span class="secondary">WORKPLACE SERVICES</span>
    </div>
  </section>

  <section class="card card-front" aria-label="Business card front">
    <div class="front-brand">
      <div class="brand-name">
        <span class="primary">CORVANE</span>
        <span class="secondary">WORKPLACE SERVICES</span>
      </div>
    </div>
    <div class="front-details">
      <div class="photo-placeholder" role="img" aria-label="Card holder profile photo">
        <div class="photo-frame"><span class="photo-label">PHOTO</span></div>
      </div>
      <p class="holder-name">CARD HOLDER NAME</p>
      <div class="divider"></div>
      <p class="phone">Tel. 01632 960418</p>
      <p class="address">Fenwick Lodge<br>Mill Lane, Ashcombe Vale, KT14 3WB</p>
    </div>
  </section>

</body>
</html>
```